Website redesign

Looking to redesign our existing website. (hire4ward.com.au)
New design needs to be bright, fun and have an easy flowing.
The website needs to be design with call to action.

Some examples of other websites:
brightdesk.com
lendnest.com.au

We are happy with the content of our existing website.

Target Market(s)

other businesses

Industry/Entity Type

Business Service

Number of Pages Required

5+ page

Requirements
Must have
• Theme redesign
Cool animation similar to brightdesk.com

```html
<!DOCTYPE html>
<html lang="en">
<head>
<meta charset="utf-8">
<title>Hire 4Ward — Virtual Assistants</title>
<link href="https://fonts.googleapis.com/css2?family=Montserrat:wght@300;400;500;600&display=swap" rel="stylesheet">
<style>
:root{
  --blue:#3184f0;
  --blue-dark:#2a73d6;
  --coral:#fd866c;
  --coral-soft:rgba(253,134,108,.8);
  --ink:#222;
  --muted:#555;
  --rule:#e2e2e2;
  --bar:#333;
  --white:#fff;
}
*{box-sizing:border-box;margin:0;padding:0}
html,body{width:1200px;height:2174px;overflow:hidden}
body{font-family:"Montserrat",Arial,sans-serif;color:var(--ink);background:var(--white);position:relative;font-weight:400}
.abs{position:absolute}

/* header */
.site-header{position:absolute;left:0;top:0;width:1200px;height:50px;border-bottom:2px solid var(--rule);background:var(--white)}
.brand{position:absolute;left:225px;top:8px;display:flex;flex-direction:column;align-items:center;width:110px}
.brand-mark{font-size:20px;font-weight:600;letter-spacing:.5px;line-height:22px;display:flex;align-items:center;gap:4px}
.brand-mark i{display:inline-block;width:10px;height:10px;border-radius:50%;background:var(--blue)}
.brand-name{font-size:10px;font-weight:600;letter-spacing:.2px}
.main-nav{position:absolute;top:18px;left:408px;display:flex;gap:0;font-size:10px;color:#333}
.main-nav a{color:inherit;text-decoration:none;margin-right:26px}
.call-pill{position:absolute;left:781px;top:14px;width:194px;height:21px;border-radius:11px;background:var(--coral);overflow:hidden}
.call-pill .call-label{position:absolute;left:0;top:0;width:97px;height:21px;border-radius:11px;background:var(--blue);color:#fff;font-size:12px;line-height:21px;padding-left:12px}
.call-pill .call-label svg{position:absolute;right:6px;top:2px}
.call-pill .call-num{position:absolute;left:113px;top:0;line-height:21px;font-size:12px;font-weight:600;color:#f4531f}

/* hero */
.hero-title{left:225px;top:202px;font-size:31px;font-weight:400;color:var(--blue);letter-spacing:-.3px}
.hero-sub{left:226px;top:250px;font-size:21px;font-weight:400;color:#222}
.btn{display:block;border-radius:16px;background:var(--blue);color:#fff;text-align:center;text-decoration:none}
.hero-cta{left:225px;top:295px;width:156px;height:31px;line-height:31px;font-size:15px}
.hero-art{left:565px;top:100px;width:605px;height:355px;border-radius:50% 50% 40% 40%;background:radial-gradient(ellipse at 55% 60%,#eef0fb 0%,#dfe3f6 45%,#c9d2f2 70%,rgba(255,255,255,0) 72%)}

/* intro band */
.intro{left:0;top:485px;width:1200px;height:277px;background:var(--coral)}
.intro h2{position:absolute;left:225px;top:28px;font-size:21px;font-weight:400;color:#fff;letter-spacing:-.3px}
.intro h2 .hl{color:var(--blue)}
.intro p{position:absolute;left:226px;top:61px;width:342px;font-size:11px;line-height:17px;color:#fff}
.video{position:absolute;left:631px;top:68px;width:344px;height:177px;background:#fff}
.video svg{position:absolute;left:130px;top:40px}

/* process */
.process{left:0;top:762px;width:1200px;height:356px;background:var(--blue)}
.process h2{position:absolute;width:1200px;top:26px;text-align:center;font-size:21px;font-weight:400;color:#fff}
.timeline{position:absolute;left:0;top:108px;width:1200px;height:1px;background:rgba(255,255,255,.7)}
.step{position:absolute;border-radius:50%;background:var(--coral);box-shadow:0 3px 6px rgba(0,0,0,.25);color:rgba(255,255,255,.85);text-align:center;display:flex;flex-direction:column;justify-content:center;line-height:1.35}
.card{position:absolute;background:var(--coral-soft);color:#fff;overflow:hidden}
.card h3{font-weight:500}
.card.main{background:var(--coral);box-shadow:0 3px 8px rgba(0,0,0,.2)}

/* services */
.services-title{width:1200px;left:0;top:1145px;text-align:center;font-size:21px;font-weight:400}
.services-lead{width:1200px;left:0;top:1174px;text-align:center;font-size:14.5px}
.services-ask{width:1200px;left:0;top:1199px;text-align:center;font-size:14px;color:var(--blue)}
.service-icon{position:absolute;width:134px;height:134px;border-radius:50%;border:2px solid var(--blue);top:1244px}
.service-icon span{position:absolute;left:10px;top:10px;width:110px;height:110px;border-radius:50%;background:var(--blue)}
.service-copy{position:absolute;top:1386px;width:260px;text-align:center;font-size:11px;line-height:24px;color:#333}

/* quote */
.quote{left:0;top:1505px;width:1200px;height:438px;background:var(--blue);color:#fff}
.quote h2{position:absolute;left:224px;top:27px;font-size:21px;font-weight:400}
.quote .lead{position:absolute;left:226px;top:62px;width:300px;font-size:12px;line-height:19px}
.perks{position:absolute;left:226px;top:122px;list-style:none;font-size:12.5px}
.perks li{display:flex;align-items:center;gap:8px;height:31.4px}
.quote-form{position:absolute;left:599px;top:32px;width:376px;height:375px;background:#fff}
.field{position:absolute;left:32px;width:312px;height:21px;border-radius:11px;background:var(--coral);border:1px solid var(--blue);overflow:hidden}
.field .label{position:absolute;left:0;top:0;width:134px;height:19px;border-radius:10px;background:var(--blue);font-size:12px;line-height:19px;padding-left:5px;color:#fff}
.field .label svg{position:absolute;right:7px;top:1px}
.field.area{height:99px;border-radius:10px}
.field.area .label{width:312px;height:37px;border-radius:9px;line-height:15px;padding-top:3px;padding-left:6px}
.field.area .label svg{top:6px;right:6px}
.newsletter{position:absolute;left:32px;top:340px;font-size:12px;color:var(--blue);display:flex;align-items:center;gap:7px}
.newsletter i{display:inline-block;width:11px;height:11px;border:1px solid var(--blue);border-radius:50%}
.submit{position:absolute;left:244px;top:338px;width:100px;height:20px;line-height:20px;font-size:12.5px;border-radius:10px}

/* footer */
.footer-col{position:absolute;top:1972px;font-size:8.5px;line-height:14.3px;color:#333}
.footer-col h4{font-size:10.5px;font-weight:500;margin-bottom:12px;color:#222}
.footer-col a{color:var(--blue);text-decoration:none}
.footer-col ul{list-style:none}
.footer-brand{left:522px;top:2090px;width:100px}
.legal-bar{left:0;top:2143px;width:1200px;height:31px;background:var(--bar);color:#fff;font-size:8px}
.legal-bar span{position:absolute;top:10px}
</style>
</head>
<body>

<header class="site-header">
  <div class="brand">
    <div class="brand-mark">H4W<i></i></div>
    <div class="brand-name">HIRE 4WARD</div>
  </div>
  <nav class="main-nav">
    <a href="#">HOME</a><a href="#">OUR STORY</a><a href="#">TIPS AND TRICKS</a><a href="#">CONTACT US</a><a href="#">FAQ</a>
  </nav>
  <div class="call-pill">
    <span class="call-label">CALL US
      <svg width="17" height="17" viewBox="0 0 17 17"><circle cx="8.5" cy="8.5" r="7.5" fill="none" stroke="#fff"/><path d="M7 5l3.5 3.5L7 12" fill="none" stroke="#fff"/></svg>
    </span>
    <span class="call-num">07 3000 4188</span>
  </div>
</header>

<section>
  <h1 class="abs hero-title">VIRTUAL ASSISTANT?</h1>
  <p class="abs hero-sub">MORE LIKE VALUABLE ASSET!</p>
  <a class="abs btn hero-cta" href="#">GET A QUOTE</a>
  <div class="abs hero-art" role="img" aria-label="Isometric illustration of a clock platform surrounded by office workstations and staff"></div>
</section>

<section class="abs intro">
  <h2><span class="hl">Outsourcing.</span> A big word that means big things <span class="hl">for your business.</span></h2>
  <p>Virtual Assistants are the superheroes of the modern office. They can do everything your team can do on a computer at a fraction of the price! (Well, maybe not high five you when you've had a win, but a virtual high five is definitely on the table!)</p>
  <div class="video">
    <svg width="84" height="96" viewBox="0 0 84 96"><path d="M1 1L82 48 1 95Z" fill="none" stroke="#333" stroke-width="1"/></svg>
  </div>
</section>

<section class="abs process">
  <h2>THE PROCCES</h2>
  <div class="timeline"></div>
  <div class="step" style="left:226px;top:85px;width:48px;height:48px;font-size:9px">Step<br>5</div>
  <div class="step" style="left:395px;top:82px;width:54px;height:54px;font-size:12px">Step<br>1</div>
  <div class="step" style="left:570px;top:78px;width:60px;height:60px;font-size:14px">Step<br>2</div>
  <div class="step" style="left:751px;top:82px;width:54px;height:54px;font-size:12px">Step<br>3</div>
  <div class="step" style="left:926px;top:85px;width:48px;height:48px;font-size:9px">Step<br>4</div>

  <div class="card" style="left:226px;top:205px;width:104px;height:73px;padding:3px 5px;font-size:5px;line-height:9px">
    <h3 style="font-size:7.5px;line-height:12px">Your Magical Journey Begins</h3>
    Now you and your Virtual Assistant are ready to rumble! Feel the magic of having an assistant take on tasks so you can focus on growth.
  </div>
  <div class="card" style="left:325px;top:183px;width:120px;height:117px;padding:3px 6px;font-size:5px;line-height:9px">
    <h3 style="font-size:8.5px;line-height:12px">Provide Your Preferred Qualities</h3>
    Set up a call with our team to share the skills you need in a Virtual Assistant. We then handle the search, testing and checks.
  </div>
  <div class="card" style="left:765px;top:183px;width:130px;height:117px;padding:3px 4px;font-size:5px;line-height:9px;text-align:left">
    <h3 style="font-size:8.5px;line-height:12px">The Final Interview</h3>
    The perfect time to get to know them. Prepare a list of questions so you pick out the chosen one.
  </div>
  <div class="card" style="left:893px;top:203px;width:82px;height:73px;padding:3px 3px;font-size:5px;line-height:9px">
    <h3 style="font-size:7px;line-height:12px">Tools</h3>
    Your Virtual Assistant is ready to start. Bring your own IT or we set it up for you.
  </div>
  <div class="card main" style="left:444px;top:158px;width:321px;height:167px;padding:10px 12px">
    <h3 style="font-size:12px;margin-bottom:6px">Endorsing the Shortlisted Candidates</h3>
    <p style="font-size:9.5px;line-height:23px">After the thorough vetting process, we'll put forward the best candidate. You can then conduct the final interview on your preferred communication platform at a time that suits you. Once the schedule is set, we'll let the candidates know!</p>
  </div>
</section>

<section>
  <h2 class="abs services-title">OUR SERVICES</h2>
  <p class="abs services-lead">We'll help you save tens (or even hundreds!) of thousands of dollars per year. But what do WE actually do?</p>
  <p class="abs services-ask">GLAD YOU ASKED!</p>

  <div class="service-icon" style="left:288px"><span role="img" aria-label="Illustration of a recruiter reviewing candidate profiles"></span></div>
  <div class="service-icon" style="left:533px"><span role="img" aria-label="Illustration of a phone being set up with a spanner and gear"></span></div>
  <div class="service-icon" style="left:778px"><span role="img" aria-label="Illustration of a gold award ribbon with a star"></span></div>

  <p class="service-copy" style="left:225px">We recruit Virtual Assistants<br>(a.k.a office legends!)<br>, andprovide the tech support<br>for these superheroes!</p>
  <p class="service-copy" style="left:469px">Set up the phone system<br>(their own Bat Phone!)</p>
  <p class="service-copy" style="left:715px">We manage Virtual Assistants and keep<br>them in tip-top shape!</p>
</section>

<section class="abs quote">
  <h2>GET A QUOTE</h2>
  <p class="lead">Fill in the form below to get a Quote for your own personal Virtual Assistant</p>
  <ul class="perks">
    <li><svg width="21" height="21" viewBox="0 0 21 21"><circle cx="10.5" cy="10.5" r="9.5" fill="#fff" stroke="#f05a3c" stroke-width="2"/><path d="M6 10.5l3 3 6-6.5" fill="none" stroke="#f05a3c" stroke-width="2"/></svg>Your Own Virtual Assistant</li>
    <li><svg width="21" height="21" viewBox="0 0 21 21"><circle cx="10.5" cy="10.5" r="9.5" fill="#fff" stroke="#f05a3c" stroke-width="2"/><path d="M6 10.5l3 3 6-6.5" fill="none" stroke="#f05a3c" stroke-width="2"/></svg>One Invoice Per Month</li>
    <li><svg width="21" height="21" viewBox="0 0 21 21"><circle cx="10.5" cy="10.5" r="9.5" fill="#fff" stroke="#f05a3c" stroke-width="2"/><path d="M6 10.5l3 3 6-6.5" fill="none" stroke="#f05a3c" stroke-width="2"/></svg>No Super or TAX</li>
    <li><svg width="21" height="21" viewBox="0 0 21 21"><circle cx="10.5" cy="10.5" r="9.5" fill="#fff" stroke="#f05a3c" stroke-width="2"/><path d="M6 10.5l3 3 6-6.5" fill="none" stroke="#f05a3c" stroke-width="2"/></svg>Dedicated To Your Business Only</li>
    <li><svg width="21" height="21" viewBox="0 0 21 21"><circle cx="10.5" cy="10.5" r="9.5" fill="#fff" stroke="#f05a3c" stroke-width="2"/><path d="M6 10.5l3 3 6-6.5" fill="none" stroke="#f05a3c" stroke-width="2"/></svg>Dedicated Phone System</li>
    <li><svg width="21" height="21" viewBox="0 0 21 21"><circle cx="10.5" cy="10.5" r="9.5" fill="#fff" stroke="#f05a3c" stroke-width="2"/><path d="M6 10.5l3 3 6-6.5" fill="none" stroke="#f05a3c" stroke-width="2"/></svg>IT Setup and Support</li>
  </ul>

  <form class="quote-form">
    <div class="field" style="top:19px"><span class="label">Bussniess Name<svg width="17" height="17" viewBox="0 0 17 17"><circle cx="8.5" cy="8.5" r="7.5" fill="none" stroke="#fff"/><path d="M7 5l3.5 3.5L7 12" fill="none" stroke="#fff"/></svg></span></div>
    <div class="field" style="top:59px"><span class="label">First Name<svg width="17" height="17" viewBox="0 0 17 17"><circle cx="8.5" cy="8.5" r="7.5" fill="none" stroke="#fff"/><path d="M7 5l3.5 3.5L7 12" fill="none" stroke="#fff"/></svg></span></div>
    <div class="field" style="top:99px"><span class="label">Surname<svg width="17" height="17" viewBox="0 0 17 17"><circle cx="8.5" cy="8.5" r="7.5" fill="none" stroke="#fff"/><path d="M7 5l3.5 3.5L7 12" fill="none" stroke="#fff"/></svg></span></div>
    <div class="field" style="top:139px"><span class="label">Contact Number<svg width="17" height="17" viewBox="0 0 17 17"><circle cx="8.5" cy="8.5" r="7.5" fill="none" stroke="#fff"/><path d="M7 5l3.5 3.5L7 12" fill="none" stroke="#fff"/></svg></span></div>
    <div class="field" style="top:179px"><span class="label">Email<svg width="17" height="17" viewBox="0 0 17 17"><circle cx="8.5" cy="8.5" r="7.5" fill="none" stroke="#fff"/><path d="M7 5l3.5 3.5L7 12" fill="none" stroke="#fff"/></svg></span></div>
    <div class="field area" style="top:219px"><span class="label">Describe the tasks you'll need from your<br>Virtual Assistant<svg width="25" height="25" viewBox="0 0 25 25"><circle cx="12.5" cy="12.5" r="11.5" fill="none" stroke="#fff"/><path d="M7.5 10l5 5 5-5" fill="none" stroke="#fff"/></svg></span></div>
    <label class="newsletter"><i></i>Subscribe to our newsletter</label>
    <a class="btn submit" href="#">Submit</a>
  </form>
</section>

<footer>
  <div class="footer-col" style="left:225px;width:200px">
    <h4>ABOUT US</h4>
    <p>Lorem ipsum dolor sit amet, consectetur adipiscing elit, sed do eiusmod tempor incididunt ut labore et dolore magna aliqua. Quis ipsum suspendisse ultrices gravida. Risus commodo viverra maecenas accumsan lacus vel facilisis.</p>
  </div>
  <div class="footer-col" style="left:537px">
    <h4>QUICK LINKS</h4>
    <ul><li>HOME</li><li>OUR STORY</li><li>TIPS AND TRICKS</li><li>CONTACT US</li><li>FAQ</li></ul>
  </div>
  <div class="abs brand footer-brand">
    <div class="brand-mark">H4W<i></i></div>
    <div class="brand-name">HIRE 4WARD</div>
  </div>
  <div class="footer-col" style="left:847px">
    <h4>CONTACT</h4>
    <p>Nina Perez<br>Mobile: 0400 555 102<br>Email:<br><a href="#">nina@hire4ward.com.au</a></p>
    <p style="margin-top:14px">Tom Lindqvist<br>Mobile: 0400 555 217<br>Email:<br><a href="#">tom@hire4ward.com.au</a></p>
  </div>
  <div class="abs legal-bar">
    <span style="left:225px">© 2019 HIRE 4WARD | ALL RIGHTS RESERVED.</span>
    <span style="left:812px">Terms of Service / Privacy Policy / Contact Us</span>
  </div>
</footer>

</body>
</html>
```